Website for Ravok Capital

We need a new web design for a company based in Chicago called "Ravok Capital". Ravok provides portfolio management and financial advice using primarily income oriented strategies, such as, dividend paying stocks and preferred stocks. Our niche is utilizing conservative option strategies to help generate income and minimize risk. We are looking for a clean-cut and streamline professional site that is both appealing and user friendly. We would like the main colors to be the dark blue and bright green of our logo. Depending on cost and ease, we may want a designer to give us the completed website, including the coding, etc.

Target Market(s)

20-80 year old affluent investors seeking portfolio management and investment advice.

Industry/Entity Type

Conservative

Requirements
Must have
• -our logo
-main tabs: home, about us, our philosophy, our services, investment strategy, compliance, contact us
-our phone number visible and conveniently placed on each page
Nice to have
• -conveniently placed login button for current clients
-conveniently placed "quick contact" box on home page with spaces for first name, last name, email, phone number, and a blank box for their question or comment
-check us out on Facebook and Twitter logos/buttons
-we like the idea of rotating pictures on top of page, but we aren't sure whether or not we definitely want that
Should not have
• -no trees
-no clocks
-no timers
-no crowns
-no plants

```html
<!DOCTYPE html>
<html lang="en">
<head>
<meta charset="utf-8">
<title>Ravok Capital</title>
<link rel="stylesheet" href="https://fonts.googleapis.com/css2?family=Source+Sans+3:wght@400;600;700&display=swap">
<style>
:root{
  --navy:#2b2f86;
  --navy-dark:#1f2370;
  --green:#5aa63a;
  --green-text:#5c9a34;
  --map-green:#5f9f70;
  --map-pale:#dde7dd;
  --ink:#222;
  --muted:#444;
  --line:#d6d9dc;
  --field:#f1f4f6;
  --card:#f5f5f5;
  --footer:#303030;
  --footer-bar:#252525;
  --footer-text:#e8e8e8;
}
*{box-sizing:border-box;margin:0;padding:0}
html,body{width:805px;height:1200px;overflow:hidden;background:#fff}
body{position:relative;font-family:"Source Sans 3",sans-serif;color:var(--ink);font-size:10px}
.abs{position:absolute}

/* header */
.brand{left:44px;top:30px;display:flex;align-items:center;gap:9px}
.brand-mark{width:22px;height:22px;border-radius:50%;background:var(--green)}
.brand-name{font-size:28px;font-weight:700;color:var(--navy);letter-spacing:.5px}
.share{right:47px;top:27px;display:flex;align-items:center;gap:5px;font-size:10.5px;color:#444}
.share span{margin-right:6px}
.share i{display:block;width:15px;height:15px;border-radius:50%}
.call{right:45px;top:59px;font-size:10.5px;color:#444}
.call b{font-weight:400;font-size:14px;color:var(--green-text);margin-left:3px}

/* nav */
.nav{left:13px;top:110px;width:774px;height:36px;display:flex;border-radius:4px;overflow:hidden;background:linear-gradient(#4a54b5,#2b3391);border:1px solid #252a7a}
.nav a{color:#fff;text-decoration:none;font-size:11px;display:flex;align-items:center;justify-content:center;border-right:1px solid #1e236a;box-shadow:inset -1px 0 0 #5660c0}
.nav a.login{background:linear-gradient(#6cbf48,#449a2c);border:none;box-shadow:none;flex:1}

/* hero */
.hero{left:13px;top:158px;width:777px;height:255px;border:1px solid #c9ccce;background:#fbfcfa;overflow:hidden}
.hero-map{position:absolute;inset:0;background:linear-gradient(90deg,var(--map-pale) 0%,var(--map-pale) 46%,var(--map-green) 52%,var(--map-green) 86%,#f4f7f4 100%)}
.hero-panel{position:absolute;left:14px;top:7px;width:283px;height:227px;background:rgba(255,255,255,.85);padding:60px 14px 0 14px}
.hero-brand{position:absolute;left:0;right:0;top:30px;text-align:center;font-size:17px;font-weight:700;color:var(--navy)}
.hero-panel h2{font-size:12px;font-weight:600;color:var(--navy);margin:23px 0 0 6px;white-space:nowrap}
.hero-panel p{font-size:9.5px;line-height:15.5px;text-align:justify;margin-top:9px;color:#111}
.btn{display:inline-block;background:var(--navy);color:#fff;font-size:11.5px;border-radius:2px;text-align:center}
.hero-panel .btn{margin-top:8px;width:99px;height:30px;line-height:30px}

/* welcome */
.welcome{left:18px;top:436px;display:flex;align-items:center;gap:10px;font-size:13px}
.welcome .brand-name{font-size:18px}
.welcome .green{color:var(--green-text)}
.team-photo{left:16px;top:479px;width:152px;height:109px;border:1px solid #bbb;background:linear-gradient(135deg,#c9c3bc,#8f8478 60%,#e9e6e3)}
.intro{left:175px;top:479px;width:338px}
.intro h3{font-size:11px;font-weight:600;color:var(--navy);margin-bottom:3px}
.intro p,.intro-more{font-size:9.5px;line-height:15.3px;text-align:justify;color:var(--muted)}
.intro-more{left:18px;top:595px;width:495px}

/* quick contact */
.qc-title{left:550px;top:434px;font-size:13px;color:#222}
.qc-title span{color:var(--green-text)}
.qc-label{left:552px;font-size:11px;color:#333}
.field{left:620px;width:161px;height:27px;background:var(--field);border:1px solid var(--line)}
.comment{left:555px;top:592px;width:226px;height:77px;background:var(--field);border:1px solid var(--line)}
.submit{left:703px;top:680px;width:78px;height:28px;line-height:28px;font-weight:700;font-size:12px;letter-spacing:.5px}

/* cards */
.card{top:724px;width:249px;height:258px;background:linear-gradient(#fff,var(--card));border:1px solid #d3d3d3;border-radius:5px}
.card h3{position:absolute;left:40px;top:14px;font-size:14.5px;font-weight:600;color:var(--navy-dark);letter-spacing:.2px}
.card-img{position:absolute;left:14px;top:52px;width:222px;height:102px;border:1px solid #c8c8c8}
.card ul{position:absolute;left:20px;top:163px;list-style:none}
.card li{font-size:9.5px;color:#333;line-height:17px;padding-left:12px;position:relative}
.card li::before{content:"";position:absolute;left:0;top:5px;border:3.5px solid transparent;border-left:5px solid var(--green)}
.read{position:absolute;right:14px;top:235px;display:flex;align-items:center;gap:6px;font-size:9.5px;color:var(--green-text);text-decoration:underline}
.read i{display:block;width:13px;height:13px;border-radius:50%;background:var(--green);position:relative}
.read i::after{content:"";position:absolute;left:5px;top:3.5px;border:3px solid transparent;border-left:4px solid #fff}

/* footer */
.footer{left:0;top:1013px;width:805px;height:138px;background:var(--footer)}
.fcol{top:1036px;color:var(--footer-text)}
.fcol h4{font-size:11.5px;font-weight:600;color:var(--green);margin-bottom:7px}
.fcol p{font-size:9.5px;line-height:15.3px}
.fcol p b{font-weight:400;color:var(--green)}
.footer-brand{left:612px;top:1055px;font-size:30px;font-weight:700;color:#3d3d3d}
.footer-bar{left:0;top:1151px;width:805px;height:49px;background:var(--footer-bar);color:#fff;font-size:10px;display:flex;justify-content:center;align-items:center;gap:14px}
</style>
</head>
<body>

<header>
  <div class="abs brand"><span class="brand-mark"></span><span class="brand-name">Ravok Capital</span></div>
  <div class="abs share"><span>Share with Us :</span><i style="background:#3b5998"></i><i style="background:#2aa9e0"></i><i style="background:#1d7ab5"></i><i style="background:#e8742c"></i></div>
  <div class="abs call">Any Question ? Call Us : <b>(312) 555-0148</b></div>
</header>

<nav class="abs nav">
  <a style="width:65px">HOME</a>
  <a style="width:74px">ABOUT US</a>
  <a style="width:110px">OUR PHILOSOPHY</a>
  <a style="width:91px">OUR SERVICES</a>
  <a style="width:134px">INVESTMENT STRATEGY</a>
  <a style="width:91px">COMPLIANCE</a>
  <a style="width:101px">CONTACT US</a>
  <a class="login">CLIENT LOGIN</a>
</nav>

<section class="abs hero">
  <div class="hero-map" role="img" aria-label="World map with continents in green"></div>
  <div class="hero-panel">
    <div class="hero-brand">Ravok Capital</div>
    <h2>LOREM IPSUM DOLOR SIT AMET CONSECTETUR</h2>
    <p>Nam pretium magna quis mauris semper fringilla ac sed leo. Fusce et justo eu est lobortis condimentum. Pellentesque et euismod neque. Pellentesque habitant morbi tristique senectus et netus et malesuada tristique vel.</p>
    <span class="btn">LEARN MORE</span>
  </div>
</section>

<section>
  <div class="abs welcome"><span>WELCOME TO</span><span class="brand-name">Ravok</span><span class="green">INVESTMENT</span></div>
  <div class="abs team-photo" role="img" aria-label="Advisors meeting with clients at a desk"></div>
  <div class="abs intro">
    <h3>LOREM IPSUM DOLOR SIT AMET CONSECTETUR</h3>
    <p>Nam pretium magna quis mauris semper fringilla ac sed leo. Fusce et justo eu est lobortis condimentum. Pellentesque et euismod neque. Pellentesque habitant morbi tristique senectus et netus et malesuada fames ac turpis egestas. Cras nec sapien risus. Curabitur Pellentesque habitant morbi tristique senectus et netus nunc sem, auctor consectetur tristique vel, accumsan sed nibh. Phasellus a fringilla magna</p>
  </div>
  <p class="abs intro-more">Nam pretium magna quis mauris semper fringilla ac sed leo. Fusce et justo eu est lobortis condimentum. Pellentesque et euismod neque. Pellentesque habitant morbi tristique senectus et netus et malesuada fames ac turpis egestas. Cras nec sapien risus. Curabitur nunc sem, auctor consectetur tristique vel, accumsan sed nibh. Phasellus a fringilla magna</p>
</section>

<form>
  <div class="abs qc-title">QUICK <span>CONTACT</span></div>
  <div class="abs qc-label" style="top:464px">Name</div><div class="abs field" style="top:458px"></div>
  <div class="abs qc-label" style="top:501px">Email id</div><div class="abs field" style="top:495px"></div>
  <div class="abs qc-label" style="top:537px">Phone</div><div class="abs field" style="top:531px"></div>
  <div class="abs qc-label" style="top:571px;left:554px">Comments</div><div class="abs comment"></div>
  <span class="abs btn submit">SUBMIT</span>
</form>

<section>
  <article class="abs card" style="left:15px">
    <h3>FINANCIAL ADVICE</h3>
    <div class="card-img" role="img" aria-label="Family planning finances together" style="background:linear-gradient(135deg,#e9dccb,#b99b7b 55%,#f2ece4)"></div>
    <ul><li>When should I plan for Retirement?</li><li>Why should I save regularly?</li><li>I have a Lump sum amount for investment</li><li>What happens to my Superannuation?</li></ul>
    <span class="read">Read More<i></i></span>
  </article>
  <article class="abs card" style="left:276px">
    <h3>INVESTMENT STRATEGY</h3>
    <div class="card-img" role="img" aria-label="Calculator on financial papers" style="background:linear-gradient(135deg,#c8ccd2,#8c939c 50%,#e4e6e8)"></div>
    <ul><li>When should I plan for Retirement?</li><li>Why should I save regularly?</li><li>I have a Lump sum amount for investment</li><li>What happens to my Superannuation?</li></ul>
    <span class="read">Read More<i></i></span>
  </article>
  <article class="abs card" style="left:539px">
    <h3>PORTFOLIO MANAGEMENT</h3>
    <div class="card-img" role="img" aria-label="Globe opened as a file drawer of folders" style="background:radial-gradient(circle at 50% 50%,#7fa6c9 0,#c9b25c 25%,#f6f6f6 45%,#ffffff 70%)"></div>
    <ul><li>When should I plan for Retirement?</li><li>Why should I save regularly?</li><li>I have a Lump sum amount for investment</li><li>What happens to my Superannuation?</li></ul>
    <span class="read">Read More<i></i></span>
  </article>
</section>

<footer>
  <div class="abs footer"></div>
  <div class="abs fcol" style="left:35px"><h4>OUR SERVICES</h4><p>Curabitur feugiat<br>mattissa ienphare<br>cursus elit obortis<br>Ornare amron</p></div>
  <div class="abs fcol" style="left:163px"><h4>USEFUL LINKS</h4><p>Curabitur feugiat<br>mattissa ienphare<br>cursus elit obortis<br>Ornare amron</p></div>
  <div class="abs fcol" style="left:287px"><h4>OUR SOLUTIONS</h4><p>Curabitur feugiat<br>mattissa ienphare<br>cursus elit obortis<br>Ornare amron</p></div>
  <div class="abs fcol" style="left:424px"><h4>CONTACT US</h4><p>Lorem ipsum dolor sit amet consrtut<br>2210 W Lake St<br>Chicago, Illinois<br>Phone: <b>(312) 555-0172</b><br>Fax: <b>(312) 555-0172</b></p></div>
  <div class="abs footer-brand">Ravok Capital</div>
  <div class="abs footer-bar"><span>Copyright 2013</span><span>|</span><span>All Rights Reserved</span><span>|</span><span>Privacy Policy</span></div>
</footer>

</body>
</html>
```